Trade show banner and popup for Forge Cloud

Use the existing logo and graphic elements and text of sales arguments from our web site www.forgecloud-example.com to create a backdrop banner and popup banner.

Both banners are trim size 181.7 x 76.2 cm. One is vertical, the other is horizontal. The full bleed size is 767 x 1824 mm 2265 x 5385 pixels.

We have a 2m by 2m corner stand on a tradeshow. The banner will be on one wall, the vertical against the other wall by the aisle.

Target Market(s)

This display is for a manufacturing trade show. The typical visitors are middle age engineers.

Industry/Entity Type

Trade

Requirements
Must have
• Our logo.
Nice to have
• One of the main benefits of our system is that it can be created for no charge with an online signup which is available at the show. We want to tempt people off the aisles to do this. So the vertical banner could have the words "Create your own online ERP system here for no charge"
Should not have
• Small text, these banners should attract attention of passers by in a trade show.

```html
<!DOCTYPE html>
<html lang="en">
<head>
<meta charset="utf-8">
<title>Forge Cloud – Trade Show Banners</title>
<link href="https://fonts.googleapis.com/css2?family=Cabin:wght@400;500;600&display=swap" rel="stylesheet">
<style>
  :root {
    --board-light: #e6e6e6;
    --board-dark: #b9b9b9;
    --teal-deep: #08394a;
    --teal-mid: #0d5d72;
    --teal-glow: #19b8e6;
    --ink: #121212;
    --gold-light: #d8cf98;
    --gold: #b9ab74;
    --gold-dark: #7d6f4f;
    --panel: #5d8e9c;
    --white: #ffffff;
  }
  * { margin: 0; padding: 0; box-sizing: border-box; }
  html, body { width: 1200px; height: 1000px; overflow: hidden; }
  body {
    position: relative;
    font-family: "Cabin", "Candara", sans-serif;
    background: radial-gradient(ellipse at 62% 55%, var(--board-light) 0%, var(--board-dark) 85%);
  }
  .banner { position: absolute; overflow: hidden; }
  .banner__bg { position: absolute; inset: 0; width: 100%; height: 100%; }

  /* Vertical popup banner */
  .popup { left: 72px; top: 57px; width: 376px; height: 893px; }
  .brand { position: absolute; display: flex; align-items: center; }
  .brand__dot {
    border-radius: 50%;
    background: var(--gold-light);
    border: 4px solid var(--ink);
    flex-shrink: 0;
  }
  .brand__name {
    color: var(--ink);
    font-weight: 500;
    line-height: 0.9;
  }
  .popup .brand { left: 18px; top: 72px; }
  .popup .brand__dot { width: 84px; height: 84px; margin-right: 14px; }
  .popup .brand__name { font-size: 46px; }

  .popup__headline {
    position: absolute; left: 0; top: 248px; width: 100%;
    text-align: center;
    font-size: 51px; font-weight: 400; line-height: 64px;
    color: var(--ink);
    letter-spacing: 0.5px;
  }
  .popup__highlight { color: var(--gold); }
  .popup__offer {
    position: absolute; left: 0; top: 518px; width: 100%;
    text-align: center; color: var(--gold);
  }
  .popup__offer-big {
    display: block; font-size: 220px; line-height: 200px; font-weight: 400;
    color: var(--gold-light);
    text-shadow: 0 0 18px rgba(216, 207, 152, 0.35);
  }
  .popup__offer-small {
    display: block; font-size: 78px; line-height: 80px; margin-top: 2px;
    color: var(--gold-dark);
  }

  /* Horizontal backdrop banner */
  .backdrop { left: 470px; top: 188px; width: 700px; height: 295px; }
  .backdrop .brand { left: 192px; top: 24px; }
  .backdrop .brand__dot { width: 72px; height: 72px; margin-right: 12px; }
  .backdrop .brand__name { font-size: 40px; }

  .backdrop__panel {
    position: absolute; left: 11px; top: 119px; width: 350px; height: 124px;
    border-radius: 8px;
    background: linear-gradient(180deg, #6f9fac 0%, var(--panel) 60%, #4d7f8e 100%);
    border: 1px solid rgba(255,255,255,0.35);
    box-shadow: 0 2px 6px rgba(0,0,0,0.35);
    padding: 8px 10px;
    color: var(--white);
    font-size: 25px; line-height: 38px;
  }
  .backdrop__benefits {
    position: absolute; left: 375px; top: 124px;
    list-style: none;
    color: var(--ink); font-size: 25px; line-height: 40px;
  }
  .backdrop__tagline {
    position: absolute; right: 18px; top: 246px;
    color: var(--ink); font-size: 25px; line-height: 40px;
  }
</style>
</head>
<body>

  <section class="banner popup" aria-label="Vertical popup banner">
    <svg class="banner__bg" viewBox="0 0 376 893" preserveAspectRatio="none" aria-hidden="true">
      <defs>
        <radialGradient id="popupGlow" cx="0.5" cy="0" r="1" fx="0.5" fy="0">
          <stop offset="0" stop-color="var(--teal-glow)"/>
          <stop offset="0.35" stop-color="var(--teal-mid)"/>
          <stop offset="1" stop-color="var(--teal-deep)"/>
        </radialGradient>
      </defs>
      <rect width="376" height="893" fill="url(#popupGlow)"/>
    </svg>
    <div class="brand">
      <span class="brand__dot"></span>
      <span class="brand__name">Forge<br>Cloud</span>
    </div>
    <h1 class="popup__headline">CREATE YOUR<br>OWN ONLINE<br><span class="popup__highlight">ERP</span> SYSTEM<br>HERE FOR</h1>
    <p class="popup__offer">
      <span class="popup__offer-big">NO</span>
      <span class="popup__offer-small">CHARGE</span>
    </p>
  </section>

  <section class="banner backdrop" aria-label="Horizontal backdrop banner">
    <svg class="banner__bg" viewBox="0 0 700 295" preserveAspectRatio="none" aria-hidden="true">
      <defs>
        <linearGradient id="backdropBase" x1="0" y1="0" x2="0" y2="1">
          <stop offset="0" stop-color="#0f6d86"/>
          <stop offset="0.5" stop-color="var(--teal-mid)"/>
          <stop offset="1" stop-color="#0b4c5f"/>
        </linearGradient>
        <radialGradient id="backdropArc" cx="0.45" cy="0.9" r="0.7">
          <stop offset="0" stop-color="#9fd3e0"/>
          <stop offset="0.6" stop-color="#4ea3ba"/>
          <stop offset="1" stop-color="#1a7690"/>
        </radialGradient>
      </defs>
      <rect width="700" height="295" fill="url(#backdropBase)"/>
      <path d="M0 0 H700 V80 Q350 40 0 98 Z" fill="url(#backdropArc)" opacity="0.9"/>
      <path d="M0 98 Q350 40 700 80" fill="none" stroke="#c7ecf5" stroke-opacity="0.5" stroke-width="1.5"/>
    </svg>
    <div class="brand">
      <span class="brand__dot"></span>
      <span class="brand__name">Forge<br>Cloud</span>
    </div>
    <p class="backdrop__panel">Online ERP for companies in material supply and manufacturing</p>
    <ul class="backdrop__benefits">
      <li>Designed for the Web</li>
      <li>Quick Start Application</li>
      <li>No Cost/Low Cost ERP</li>
    </ul>
    <p class="backdrop__tagline">Focused on your business needs</p>
  </section>

</body>
</html>
```